The City of Maple Hollow needs a cover for their 2020 Activities Guide

Good morning.

My name is Daniel Keeler. I am the new Executive Assistant to City Manager R. Walter Pincott in the City of Maple Hollow. In the past my predecessor, Owen Brandt has reached out to you for different projects.

I am reaching out for another project – the cover of our 2020 Activity Guide. This Activity Guide will have the different activities to do in the City of Maple Hollow for 2020.

I have attached a draft sketch of what we would like to do and an in-depth explanation of what we would like.

```html
<!DOCTYPE html>
<html lang="en">
<head>
<meta charset="utf-8">
<title>City of Maple Hollow 2020 Activity Guide – Cover</title>
<link rel="stylesheet" href="https://fonts.googleapis.com/css2?family=Barlow+Condensed:wght@700&display=swap">
<style>
  :root {
    --backdrop: #e8e5e0;
    --paper: #f0f0f0;
    --ink: #0b0b0b;
    --accent: #d90000;
    --placeholder: #8a8a8a;
  }
  html, body {
    margin: 0;
    width: 1200px;
    height: 1008px;
    overflow: hidden;
    background: var(--backdrop);
  }
  .canvas {
    position: relative;
    width: 1200px;
    height: 1008px;
  }
  .cover {
    position: absolute;
    left: 275px;
    top: 42px;
    width: 650px;
    height: 924px;
    box-shadow: 0 6px 18px rgba(0,0,0,0.18);
  }
  .cover svg { display: block; }
  .title {
    font-family: "Barlow Condensed", "Arial Narrow", sans-serif;
    font-weight: 700;
    fill: var(--ink);
  }
  .title .highlight { fill: var(--accent); }
  .brand-name {
    font-family: "Barlow Condensed", "Arial Narrow", sans-serif;
    font-weight: 700;
    fill: var(--ink);
  }
  .ink { fill: var(--ink); }
  .paper { fill: var(--paper); }
  .lens { fill: none; stroke: var(--accent); }
  .lens-handle { fill: var(--accent); }
  .placeholder { fill: var(--placeholder); }
</style>
</head>
<body>
<main class="canvas">
  <section class="cover" aria-label="City of Maple Hollow 2020 Activity Guide cover">
    <svg width="650" height="924" viewBox="530 40 890 1265" xmlns="http://www.w3.org/2000/svg">
      <defs>
        <g id="icon-basketball">
          <circle r="1" class="ink"/>
          <g fill="none" stroke="#f0f0f0" stroke-width="0.08">
            <path d="M-1 0 H1"/>
            <path d="M0 -1 V1"/>
            <path d="M-0.7 -0.7 Q-0.2 0 -0.7 0.7"/>
            <path d="M0.7 -0.7 Q0.2 0 0.7 0.7"/>
          </g>
        </g>
        <g id="icon-baseball">
          <circle r="0.95" fill="#f0f0f0" stroke="#0b0b0b" stroke-width="0.1"/>
          <g fill="none" stroke="#0b0b0b" stroke-width="0.09" stroke-dasharray="0.09 0.09">
            <path d="M-0.45 -0.82 Q-0.1 0 -0.45 0.82"/>
            <path d="M0.45 -0.82 Q0.1 0 0.45 0.82"/>
          </g>
          <g fill="none" stroke="#0b0b0b" stroke-width="0.06">
            <path d="M-0.45 -0.82 Q-0.1 0 -0.45 0.82"/>
            <path d="M0.45 -0.82 Q0.1 0 0.45 0.82"/>
          </g>
        </g>
        <g id="icon-soccer">
          <circle r="0.95" fill="#f0f0f0" stroke="#0b0b0b" stroke-width="0.12"/>
          <polygon class="ink" points="0,-0.35 0.33,-0.11 0.2,0.28 -0.2,0.28 -0.33,-0.11"/>
          <polygon class="ink" points="-0.95,-0.1 -0.6,-0.3 -0.55,0.15 -0.85,0.4"/>
          <polygon class="ink" points="0.95,-0.1 0.6,-0.3 0.55,0.15 0.85,0.4"/>
          <polygon class="ink" points="-0.25,0.92 -0.2,0.6 0.2,0.6 0.25,0.92"/>
          <polygon class="ink" points="-0.3,-0.9 0,-0.7 0.3,-0.9"/>
        </g>
        <g id="icon-books">
          <polygon class="ink" points="0,0.15 0.18,0 0.55,0.12 0.55,1 0.2,0.92 0,1.05"/>
          <polygon class="ink" points="0.45,0.2 0.62,0.05 1,0.18 1,1.05 0.62,0.98 0.45,1.1"/>
          <path d="M0.22 0.18 V0.9 M0.66 0.24 V0.96" stroke="#f0f0f0" stroke-width="0.04"/>
        </g>
        <g id="icon-school">
          <polygon class="ink" points="0.5,0 0.68,0.2 0.68,0.3 0.32,0.3 0.32,0.2"/>
          <rect class="ink" x="0.33" y="0.3" width="0.34" height="0.7"/>
          <polygon class="ink" points="0,0.55 0.1,0.45 0.33,0.45 0.33,0.6 0.02,0.6"/>
          <polygon class="ink" points="1,0.55 0.9,0.45 0.67,0.45 0.67,0.6 0.98,0.6"/>
          <rect class="ink" x="0.02" y="0.6" width="0.31" height="0.4"/>
          <rect class="ink" x="0.67" y="0.6" width="0.31" height="0.4"/>
          <circle cx="0.5" cy="0.42" r="0.04" fill="#f0f0f0"/>
          <path d="M0.42 1 V0.75 Q0.5 0.62 0.58 0.75 V1 Z" fill="#f0f0f0"/>
          <rect x="0.08" y="0.74" width="0.07" height="0.08" fill="#f0f0f0"/>
          <rect x="0.2" y="0.74" width="0.07" height="0.08" fill="#f0f0f0"/>
          <rect x="0.73" y="0.74" width="0.07" height="0.08" fill="#f0f0f0"/>
          <rect x="0.85" y="0.74" width="0.07" height="0.08" fill="#f0f0f0"/>
        </g>
        <g id="icon-mountain">
          <polygon class="ink" points="0,1 0.42,0.2 0.55,0.38 0.65,0 1,1"/>
          <path d="M0.34 0.36 L0.42 0.5 L0.47 0.4 M0.58 0.14 L0.65 0.28 L0.72 0.18" fill="none" stroke="#f0f0f0" stroke-width="0.03"/>
        </g>
        <g id="icon-bicycle">
          <circle cx="0.38" cy="0.56" r="0.38" fill="none" stroke="#0b0b0b" stroke-width="0.04"/>
          <circle cx="0.38" cy="0.56" r="0.04" class="ink"/>
          <path d="M0.38 0.18 V0.94 M0 0.56 H0.76 M0.11 0.29 L0.65 0.83 M0.65 0.29 L0.11 0.83" stroke="#0b0b0b" stroke-width="0.015"/>
          <circle cx="0.86" cy="0.85" r="0.12" fill="none" stroke="#0b0b0b" stroke-width="0.04"/>
          <path d="M0.38 0.56 L0.45 0.05 M0.3 0.05 H0.55 M0.45 0.12 Q0.8 0.3 0.86 0.85" fill="none" stroke="#0b0b0b" stroke-width="0.04"/>
        </g>
      </defs>

      <rect class="paper" x="530" y="40" width="890" height="1265"/>
      <polygon class="ink" points="530,45 720,45 530,205"/>
      <polygon class="ink" points="1420,1150 1420,1305 1245,1305"/>

      <g class="brand" aria-label="City of Maple Hollow">
        <circle cx="770" cy="190" r="72" fill="none" stroke="#0b0b0b" stroke-width="7"/>
        <text class="brand-name" x="770" y="182" font-size="24" text-anchor="middle">CITY OF</text>
        <text class="brand-name" x="770" y="210" font-size="24" text-anchor="middle">MAPLE HOLLOW</text>
      </g>

      <text class="title" x="928" y="145" font-size="76" textLength="362" lengthAdjust="spacingAndGlyphs">CITY OF <tspan class="highlight">MAPLE</tspan></text>
      <text class="title" x="930" y="202" font-size="54" textLength="276" lengthAdjust="spacingAndGlyphs">HOLLOW <tspan class="highlight">2020</tspan></text>
      <text class="title" x="930" y="258" font-size="54">ACTIVITY</text>
      <text class="title" x="930" y="316" font-size="54">GUIDE</text>

      <g class="activity-icons">
        <use href="#icon-bicycle" transform="translate(585 245) scale(105 95)"/>
        <use href="#icon-bicycle" transform="translate(582 925) scale(105 95)"/>
        <use href="#icon-books" transform="translate(702 340) scale(64 62)"/>
        <use href="#icon-books" transform="translate(976 935) scale(64 55)"/>
        <use href="#icon-basketball" transform="translate(590 402) scale(28)"/>
        <use href="#icon-basketball" transform="translate(1305 600) scale(52)"/>
        <use href="#icon-basketball" transform="translate(1385 548) scale(22)"/>
        <use href="#icon-basketball" transform="translate(1378 895) scale(28)"/>
        <use href="#icon-basketball" transform="translate(718 1238) scale(28)"/>
        <use href="#icon-soccer" transform="translate(848 430) scale(29)"/>
        <use href="#icon-soccer" transform="translate(1093 1135) scale(30)"/>
        <use href="#icon-baseball" transform="translate(907 487) scale(27)"/>
        <use href="#icon-baseball" transform="translate(714 531) scale(29)"/>
        <use href="#icon-school" transform="translate(585 775) scale(180 105)"/>
        <use href="#icon-school" transform="translate(1083 985) scale(180 100)"/>
        <use href="#icon-mountain" transform="translate(1263 325) scale(137 75)"/>
        <use href="#icon-mountain" transform="translate(967 1190) scale(135 75)"/>

        <rect class="placeholder" x="560" y="540" width="90" height="52" rx="8" role="img" aria-label="Swimmer icon"/>
        <rect class="placeholder" x="1105" y="1168" width="86" height="58" rx="8" role="img" aria-label="Swimmer icon"/>
        <circle class="placeholder" cx="1195" cy="360" r="45" role="img" aria-label="Hiker icon"/>
        <circle class="placeholder" cx="1318" cy="1122" r="45" role="img" aria-label="Hiker icon"/>
        <circle class="placeholder" cx="773" cy="640" r="40" role="img" aria-label="Labyrinth pattern icon"/>
        <circle class="placeholder" cx="1345" cy="990" r="40" role="img" aria-label="Labyrinth pattern icon"/>
        <rect class="placeholder" x="605" y="645" width="70" height="75" rx="30" role="img" aria-label="Rock cairn icon"/>
        <rect class="placeholder" x="765" y="1090" width="70" height="65" rx="28" role="img" aria-label="Rock cairn icon"/>
        <circle class="ink" cx="1066" cy="370" r="32"/>
        <circle class="ink" cx="971" cy="1143" r="32"/>
        <text class="brand-name" x="968" y="1080" font-size="40" text-anchor="middle">LIBERTY WALL</text>

        <use href="#icon-baseball" transform="translate(1010 575) scale(62)"/>
        <use href="#icon-books" transform="translate(1000 740) scale(152 135)"/>
      </g>

      <g class="magnifier">
        <circle class="lens" cx="1130" cy="690" r="256" stroke-width="62"/>
        <path class="lens-handle" d="M945 850 L985 890 L850 1030 L810 990 Z"/>
        <rect class="lens-handle" x="560" y="1050" width="330" height="110" rx="30" transform="rotate(-45 725 1105)"/>
      </g>
    </svg>
  </section>
</main>
</body>
</html>
```